New travel store signage for Kelvane Journeys to attract luxury travellers.

Hello,
We are looking to change the signage of our stores. The signage must include the following:
1. Kelvane Journeys Logo (attached)
2. The text...The Travel & Cruise Experts
3. Brand Colours ( Fb0196, 412266, d41d84 and ffffff)
Please note the signage design must be central and only cover two thirds of the store front. We have also attached an image of one of our new stores which might be helpful when preparing a mock up.

We are looking for a quick turnaround on this, making a decision within 48 hours.

Target Market(s)

Retail

Industry/Entity Type

Travel Agency

Font styles to use
Other font styles liked:
• Radley

Colors
E54698
E96AAD
F1A4CE
F9D9EA
FCEFF6
6B429C
8869AF
B7A5CE
E3DAEB
F3F0F8

Requirements
Must have
• Hello, We are looking to change the signage of our stores. The signage must include the following: 1. Kelvane Journeys Logo (attached) 2. The text...The Travel & Cruise Experts 3. Brand Colours ( Fb0196, 412266, d41d84 and ffffff) Please note the signage design must be central and only cover two thirds of the store front.
Should not have
• different colour or fonts. Gradient design.

```html
<!DOCTYPE html>
<html lang="en">
<head>
<meta charset="UTF-8">
<title>Kelvane Journeys — Store Signage</title>
<link rel="stylesheet" href="https://fonts.googleapis.com/css2?family=Radley&display=swap">
<style>
  :root {
    --brand-purple: #6b429c;
    --brand-purple-deep: #5e3a92;
    --brand-pink: #e54698;
    --brand-pink-soft: #f1a4ce;
    --panel-white: #ffffff;
    --canvas-bg: #ffffff;
  }
  html, body {
    margin: 0;
    padding: 0;
    width: 1200px;
    height: 1200px;
    overflow: hidden;
    background: var(--canvas-bg);
  }
  .canvas {
    position: relative;
    width: 1200px;
    height: 1200px;
  }
  .signage {
    position: absolute;
    left: 0;
    top: 0;
    width: 1200px;
    height: 1200px;
  }
  .brand-name {
    font-family: "Radley", Georgia, serif;
    font-size: 34px;
    fill: var(--brand-purple);
  }
  .tagline {
    font-family: "Radley", Georgia, serif;
    font-size: 15px;
    letter-spacing: 0.2px;
    fill: var(--brand-purple);
  }
</style>
</head>
<body>
<div class="canvas">
  <svg class="signage" viewBox="0 0 1200 1200" xmlns="http://www.w3.org/2000/svg">
    <defs>
      <linearGradient id="ribbon-left" x1="0" y1="0" x2="1" y2="0">
        <stop offset="0" stop-color="var(--brand-purple)"/>
        <stop offset="1" stop-color="var(--brand-pink)"/>
      </linearGradient>
      <linearGradient id="ribbon-right" x1="0" y1="0" x2="1" y2="0">
        <stop offset="0" stop-color="var(--brand-pink)"/>
        <stop offset="1" stop-color="var(--brand-purple)"/>
      </linearGradient>
      <filter id="sign-shadow" x="-5%" y="-10%" width="110%" height="120%">
        <feDropShadow dx="0" dy="1" stdDeviation="1.5" flood-opacity="0.25"/>
      </filter>
    </defs>

    <!-- Sign frame -->
    <rect class="sign-frame" x="155" y="178" width="890" height="208" fill="var(--brand-purple)" filter="url(#sign-shadow)"/>
    <rect class="sign-panel" x="161" y="184" width="878" height="196" rx="8" fill="var(--panel-white)"/>
    <rect class="sign-panel-corner" x="161" y="184" width="20" height="196" fill="var(--panel-white)"/>

    <!-- Corner ribbon areas -->
    <path class="ribbon-zone ribbon-zone--left" role="img" aria-label="Flowing purple-to-pink ribbon decoration"
          d="M161 225 C 260 228, 340 300, 372 380 L 161 380 Z"
          fill="url(#ribbon-left)" opacity="0.85"/>
    <path class="ribbon-zone ribbon-zone--right" role="img" aria-label="Flowing pink-to-purple ribbon decoration"
          d="M796 184 L 1039 184 L 1039 345 C 930 350, 830 300, 796 184 Z"
          fill="url(#ribbon-right)" opacity="0.85"/>

    <!-- Brand lockup -->
    <text class="brand-name" x="621" y="320" text-anchor="middle">Kelvane Journeys</text>
    <line class="brand-rule" x1="513" y1="329" x2="727" y2="329" stroke="var(--brand-purple)" stroke-width="1.6"/>
    <text class="tagline" x="620" y="350" text-anchor="middle">THE TRAVEL &amp; CRUISE EXPERTS</text>
  </svg>
</div>
</body>
</html>
```